Business Telephone Service Brochure

I need a brochure designed to help sell our VoIP service. The brochure needs to be clean, attention getting, professional and have 3 key areas of information (Key Features, Benefits & Service Plans). Here is an idea of what we are looking for https://www.artflockly.com/design/52930487. Need to also include how much the customer could save. See this for an example https://42mockups.com/postcard-flyer-design/contests/voip-sales-flyer-template-replicate-attached-358209. The Service Plan section needs to allow room for two types of plans. One plan includes the phone and has a 12, 24 and 36 month option. Each term (12,24,36) will have its own monthly cost per device. The second service option is no-commitment monthly with a single per month price per device. The included features section should allow for up to 16 features to be listed. The benefits should allow for 4-6 benefits to be listed. Also include room for Logo, business address, website, phone number and email.

Target Market(s)

Small to medium business with 1-100 employees.

Industry/Entity Type

Telecommunications

Font styles to use
Serif

Colors

Designer to choose colors to be used in the design.

Requirements
Must have
• Key Feature, Benefits and Service Plans (i.e. Pricing). Company logo, phone, email and website. Must have "Save up to x%!" and catch attention.
Nice to have
• Limited colors. I am not setting a hard limit, please take the liberty to do what you feel is needed. Just keep in mind we want it to be clean, professional and attention getting without being to flashy or obnoxious.
Should not have
• Nothing busy or distracting.

```html
<!DOCTYPE html>
<html lang="en">
<head>
<meta charset="utf-8">
<title>Corvane VoIP Flyer</title>
<link rel="stylesheet" href="https://fonts.googleapis.com/css2?family=Lato:ital,wght@0,400;0,700;0,900;1,400;1,700&family=Arimo:wght@700&display=swap">
<style>
  :root {
    --navy: #1d1f6e;
    --royal: #2b3a9a;
    --indigo: #2d2f8c;
    --sky: #62a8f0;
    --table-blue: #2659b0;
    --dark: #262626;
    --charcoal: #333333;
    --mist: #e9eaec;
    --white: #ffffff;
    --ink: #222222;
    --stage: #3b3b3b;
  }
  * { box-sizing: border-box; margin: 0; padding: 0; }
  html, body { width: 1200px; height: 902px; overflow: hidden; }
  body { background: var(--stage); font-family: "Lato", sans-serif; position: relative; }

  .page { position: absolute; width: 514px; height: 660px; overflow: hidden; background: var(--white); box-shadow: 0 6px 18px rgba(0,0,0,.45); }
  .page--front { left: 64px; top: 99px; }
  .page--back { left: 621px; top: 126px; }
  .layer { position: absolute; inset: 0; width: 514px; height: 660px; }

  .brand { position: absolute; }
  .brand__name { font-family: "Lato", sans-serif; font-weight: 900; font-size: 46px; line-height: 1; color: var(--indigo); letter-spacing: -1px; }
  .brand__tag { font-size: 7.5px; color: #555; margin-top: 2px; letter-spacing: .2px; }
  .page--front .brand { right: 26px; top: 24px; text-align: right; }
  .page--back .brand { left: 42px; top: 38px; text-align: left; }

  .placeholder { position: absolute; }
  .photo-agent { left: 0; top: 88px; width: 275px; height: 200px; background: linear-gradient(135deg, #d9dee4, #b7c2cc 60%, #e6e9ec); clip-path: polygon(0 6%, 100% 0, 100% 100%, 0 92%); }
  .photo-desk-phone { left: 8px; top: 305px; width: 200px; height: 150px; background: radial-gradient(ellipse at 55% 50%, #5b5f66, #9a9ea5 55%, rgba(255,255,255,0) 75%); }
  .voip-graphic { left: 34px; top: 470px; width: 150px; height: 100px; background: radial-gradient(ellipse at 50% 45%, #4e8fe0, #9cc4f0 55%, rgba(255,255,255,0) 78%); }
  .photo-office-phone { left: 175px; top: 28px; width: 339px; height: 265px; background: linear-gradient(120deg, rgba(255,255,255,0) 0%, #d8dde2 20%, #9ea3aa 55%, #c9ced3 100%); }

  .offer { position: absolute; left: 270px; top: 145px; width: 230px; text-align: center; font-family: "Arimo", sans-serif; font-weight: 700; }
  .offer__lead { font-size: 34px; color: var(--white); line-height: 1.05; }
  .offer__amount { font-size: 46px; color: #a9cbf6; line-height: 1.1; text-shadow: 0 3px 4px rgba(0,0,0,.5); }

  .pill { position: absolute; height: 24px; font-size: 13px; display: flex; align-items: center; }
  .pill--features { left: 223px; top: 308px; width: 133px; background: #ececec; color: var(--ink); padding-left: 16px; border-radius: 12px; }
  .pill--benefits { left: 0; top: 116px; width: 142px; background: var(--royal); color: var(--white); padding-left: 30px; font-size: 14px; letter-spacing: .5px; border-radius: 0 14px 14px 0; }

  .features { position: absolute; left: 198px; top: 347px; list-style: none; }
  .features li { font-style: italic; font-size: 10.6px; color: var(--white); line-height: 16.3px; margin-left: calc(26px - var(--i) * 2px); position: relative; padding-left: 20px; white-space: nowrap; }
  .features li::before { content: ""; position: absolute; left: 0; top: 4.5px; width: 7px; height: 7px; border-radius: 50%; background: var(--white); }

  .benefits { position: absolute; left: 32px; top: 161px; list-style: none; }
  .benefits li { font-style: italic; font-size: 11px; color: var(--ink); line-height: 18.2px; padding-left: 16px; position: relative; }
  .benefits li::before { content: ""; position: absolute; left: 0; top: 6px; width: 6px; height: 6px; border-radius: 50%; background: var(--navy); }

  .plans { position: absolute; left: 34px; top: 338px; width: 460px; height: 176px; border-radius: 22px; background: var(--white); border: 4px solid #d6d6d6; box-shadow: 0 3px 8px rgba(0,0,0,.3); overflow: hidden; }
  .plans table { border-collapse: separate; border-spacing: 2px 0; position: absolute; left: 0; top: 18px; width: 100%; }
  .plans th, .plans td { text-align: center; color: var(--white); }
  .plans thead th { background: var(--navy); height: 40px; font-weight: 700; }
  .plans thead th.plans__title { background: var(--white); color: var(--navy); text-align: left; padding-left: 16px; font-family: "Arimo", sans-serif; font-size: 21px; line-height: .95; width: 118px; }
  .plans__title span { color: #2e8fe8; display: block; font-size: 24px; }
  .plans .term-num { display: block; font-size: 22px; line-height: 1; font-family: "Arimo", sans-serif; }
  .plans .term-label { font-size: 8.5px; letter-spacing: .2px; }
  .plans .col-monthly { font-size: 12px; }
  .plans tbody tr.gap td { height: 12px; background: var(--mist); }
  .plans tbody td { background: var(--table-blue); height: 34px; font-weight: 700; font-size: 12px; }
  .plans tbody td.plan-name { text-align: left; font-size: 9px; font-weight: 400; padding-left: 8px; line-height: 1.25; }
  .plans tbody tr.last td { height: 30px; }
  .plans .tail td { height: 20px; background: var(--mist); }

  .footnotes { position: absolute; left: 62px; top: 530px; font-size: 8px; color: var(--ink); line-height: 10.5px; }

  .contacts { position: absolute; left: 0; width: 514px; display: flex; justify-content: center; gap: 18px; align-items: center; color: var(--white); font-size: 13px; }
  .page--front .contacts { top: 613px; }
  .page--back .contacts { top: 616px; }
  .contacts__item { display: flex; align-items: center; gap: 6px; }
  .contacts svg { width: 14px; height: 14px; }
</style>
</head>
<body>

<section class="page page--front">
  <svg class="layer" viewBox="0 0 514 660" aria-hidden="true">
    <defs>
      <linearGradient id="front-sky" x1="0" y1="0" x2="0" y2="1">
        <stop offset="0" stop-color="#f2f2f2"/><stop offset="1" stop-color="#dcdcdc"/>
      </linearGradient>
      <linearGradient id="front-blue" x1="0" y1="0" x2="1" y2="1">
        <stop offset="0" stop-color="#3a47ad"/><stop offset="1" stop-color="#22287a"/>
      </linearGradient>
    </defs>
    <rect width="514" height="660" fill="url(#front-sky)"/>
    <rect y="300" width="514" height="300" fill="#ffffff"/>
    <path d="M235 95 L514 110 L514 300 L200 300 Z" fill="var(--charcoal)"/>
    <path d="M200 300 C300 360 380 310 514 250 L514 590 L150 610 C180 520 185 420 200 300 Z" fill="url(#front-blue)"/>
    <path d="M0 95 C120 60 330 55 514 130 L514 140 C330 75 120 80 0 110 Z" fill="var(--royal)"/>
    <path d="M0 260 C60 300 140 310 260 295 C360 283 440 265 514 240 L514 255 C430 285 330 305 240 312 C140 320 60 310 0 285 Z" fill="#7a7a7a"/>
    <path d="M0 525 C80 585 230 610 514 560 L514 575 C230 625 80 600 0 545 Z" fill="var(--royal)"/>
    <path d="M0 590 C120 620 300 615 514 580 L514 660 L0 660 Z" fill="var(--dark)"/>
  </svg>

  <div class="placeholder photo-agent" role="img" aria-label="Photo of a smiling support agent wearing a headset in a bright office"></div>
  <div class="placeholder photo-desk-phone" role="img" aria-label="Photo of a grey desk IP telephone with handset"></div>
  <div class="placeholder voip-graphic" role="img" aria-label="Blue VoIP lettering graphic with a globe and wireless signal"></div>

  <div class="brand">
    <div class="brand__name">corvane</div>
    <div class="brand__tag">Internet-Telephone-Security-Networking</div>
  </div>

  <div class="offer">
    <div class="offer__lead">Save up to</div>
    <div class="offer__amount">X% OFF</div>
  </div>

  <div class="pill pill--features">KEY FEATURES</div>
  <ul class="features">
    <li style="--i:0">Unlimited local and long distance calling</li>
    <li style="--i:1">HD Voice</li>
    <li style="--i:2">Business SMS/Text Messaging</li>
    <li style="--i:3">Personal and Shared Voicemail Boxes</li>
    <li style="--i:4">Audio Conferencing</li>
    <li style="--i:5">Intercom</li>
    <li style="--i:6">Mobile App</li>
    <li style="--i:7">Auto Attendant/Interactive Voice Routing</li>
    <li style="--i:8">Free web or email fax</li>
    <li style="--i:9">Web admin portal</li>
    <li style="--i:10">Music On Hold - Customizable</li>
    <li style="--i:11">Simultaneous ring / follow-me</li>
    <li style="--i:12">Redundancy/Failover – Never miss a call</li>
  </ul>

  <div class="contacts">
    <span class="contacts__item"><svg viewBox="0 0 16 16"><circle cx="8" cy="8" r="7" fill="none" stroke="#fff" stroke-width="1.3"/><path d="M5.5 4.5l1.5 1.6-.8 1c.5 1 1.3 1.8 2.3 2.3l1-.8 1.6 1.5-1 1.2C7.7 11 5 8.3 4.3 5.5z" fill="#fff"/></svg>123-456-7890</span>
    <span class="contacts__item"><svg viewBox="0 0 16 16"><rect x="1.5" y="3.5" width="13" height="9" fill="#fff"/><path d="M1.5 3.5l6.5 5 6.5-5" fill="none" stroke="#262626" stroke-width="1.2"/></svg>info@compantname.com</span>
    <span class="contacts__item"><svg viewBox="0 0 16 16" fill="none" stroke="#fff" stroke-width="1.2"><circle cx="8" cy="8" r="6.5"/><ellipse cx="8" cy="8" rx="3" ry="6.5"/><path d="M1.5 8h13"/></svg>www.websitename.com</span>
  </div>
</section>

<section class="page page--back">
  <svg class="layer" viewBox="0 0 514 660" aria-hidden="true">
    <rect width="514" height="660" fill="#ffffff"/>
    <path d="M0 235 C40 300 150 320 514 300 L514 312 C150 335 30 310 0 250 Z" fill="var(--navy)"/>
    <path d="M0 520 C30 580 140 610 514 570 L514 586 C150 625 30 600 0 545 Z" fill="var(--navy)"/>
    <path d="M0 560 C60 610 200 625 514 585 L514 660 L0 660 Z" fill="var(--navy)"/>
  </svg>

  <div class="placeholder photo-office-phone" role="img" aria-label="Photo of a black office IP phone with a smartphone and pen on a desk, city skyline behind"></div>

  <div class="brand">
    <div class="brand__name">corvane</div>
    <div class="brand__tag">Internet-Telephone-Security-Networking</div>
  </div>

  <div class="pill pill--benefits">BENEFITS</div>
  <ul class="benefits">
    <li>No expensive onsite telephone equipment</li>
    <li>Easily scale up or down and needs change</li>
    <li>Free telephone/email support</li>
    <li>Lower monthly cost</li>
    <li>Increase reliability</li>
    <li>Easy self-administration</li>
  </ul>

  <div class="plans">
    <table>
      <thead>
        <tr>
          <th class="plans__title">SERVICE<span>PLANS</span></th>
          <th class="col-monthly">MONTHLY</th>
          <th><span class="term-num">12</span><span class="term-label">MONTH TERM</span></th>
          <th><span class="term-num">24</span><span class="term-label">MONTH TERM</span></th>
          <th><span class="term-num">36</span><span class="term-label">MONTH TERM</span></th>
        </tr>
      </thead>
      <tbody>
        <tr class="gap"><td></td><td></td><td></td><td></td><td></td></tr>
        <tr>
          <td class="plan-name"><sup>1</sup>Phone service only<br>(phone sold separately)</td>
          <td>$21.95</td><td>——</td><td>——</td><td>——</td>
        </tr>
        <tr class="gap"><td></td><td></td><td></td><td></td><td></td></tr>
        <tr class="last">
          <td class="plan-name">Service + <sup>2</sup>Tellon<br>T40D Phone</td>
          <td></td><td>$24.95</td><td>$22.95</td><td>$20.95</td>
        </tr>
        <tr class="tail"><td></td><td></td><td></td><td></td><td></td></tr>
      </tbody>
    </table>
  </div>

  <p class="footnotes">
    <sup>1</sup>For monthly service you may purchase the Tellon T40D phone for $65 each, less taxes and shipping.<br>
    <sup>2</sup>Tellon T40D phones are rented and due upon cancellation. Customer pays return shipping.
  </p>

  <div class="contacts">
    <span class="contacts__item"><svg viewBox="0 0 16 16"><circle cx="8" cy="8" r="7" fill="none" stroke="#fff" stroke-width="1.3"/><path d="M5.5 4.5l1.5 1.6-.8 1c.5 1 1.3 1.8 2.3 2.3l1-.8 1.6 1.5-1 1.2C7.7 11 5 8.3 4.3 5.5z" fill="#fff"/></svg>123-456-7890</span>
    <span class="contacts__item"><svg viewBox="0 0 16 16"><rect x="1.5" y="3.5" width="13" height="9" fill="#fff"/><path d="M1.5 3.5l6.5 5 6.5-5" fill="none" stroke="#1d1f6e" stroke-width="1.2"/></svg>info@compantname.com</span>
    <span class="contacts__item"><svg viewBox="0 0 16 16" fill="none" stroke="#fff" stroke-width="1.2"><circle cx="8" cy="8" r="6.5"/><ellipse cx="8" cy="8" rx="3" ry="6.5"/><path d="M1.5 8h13"/></svg>www.websitename.com</span>
  </div>
</section>

</body>
</html>
```